Name of Business is Tidewell Vitality Mentor,
Business Card and Logo Design for a health coaching practice that brings together all aspects of living including breathing, meditation, heartfelt intentional living, oneness with others, compassion, nutrition, hydration and primary care physician.

Target Market(s)

People looking for holistic approach to optimal living.

Industry/Entity Type

Business

Contact Information for Business Card

Marcus R.T. Dunmore
CLP, CCHC, C-IQ
Tidewell Vitality Mentor
614 Birchmoor Ave
Larkspur Heights, MI 48392

Logo Text

Everything You Need Is Within You Now

```html
<!DOCTYPE html>
<html lang="en">
<head>
<meta charset="utf-8">
<title>Tidewell Vitality Mentor – Business Card</title>
<link href="https://fonts.googleapis.com/css2?family=Lato:ital,wght@0,400;0,700;1,400&family=Questrial&display=swap" rel="stylesheet">
<style>
  :root{
    --bg:#2b2b2d;
    --card:#ffffff;
    --blue:#0a74b4;
    --blue-light:#0a92cf;
    --blue-deep:#0567a3;
    --green:#4fb848;
    --white:#ffffff;
  }
  *{margin:0;padding:0;box-sizing:border-box}
  html,body{width:1200px;height:1200px;overflow:hidden;background:var(--bg)}
  .canvas{position:relative;width:1200px;height:1200px}
  .card{position:absolute;left:160px;width:880px;height:503px;background:var(--card);overflow:hidden}
  .card--front{top:70px}
  .card--back{top:627px}

  /* front */
  .brand{position:absolute;left:0;right:0;top:110px;display:flex;flex-direction:column;align-items:center;gap:22px}
  .brand__dot{width:90px;height:90px;border-radius:50%;background:var(--green)}
  .brand__name{font-family:'Questrial',sans-serif;font-size:50px;color:var(--blue);letter-spacing:.5px;line-height:1}
  .values{position:absolute;left:60px;right:60px;top:300px;text-align:center;font-family:'Lato',sans-serif;font-size:21px;line-height:1.55;color:var(--blue)}
  .values .sep{color:var(--green);margin:0 8px}

  /* back */
  .back-art{position:absolute;inset:0}
  .contact{position:absolute;left:58px;top:50px;color:var(--white);font-family:'Lato',sans-serif}
  .contact__title{font-family:'Questrial',sans-serif;line-height:.98;margin-bottom:30px}
  .contact__title .light{display:block;font-size:46px;font-weight:400}
  .contact__title .bold{display:block;font-size:46px;font-weight:700;font-family:'Lato',sans-serif;letter-spacing:1px}
  .contact__name{font-size:25px;font-weight:700;letter-spacing:1px}
  .contact__role{font-size:20px;line-height:1.3;margin-bottom:18px}
  .contact__address{font-size:20px;line-height:1.35;margin-bottom:10px}
  .contact__line{display:flex;align-items:center;gap:10px;font-size:20px;line-height:1.4}
  .contact__line svg{width:20px;height:20px;flex:none}
  .mark{position:absolute;left:540px;top:190px;width:300px;display:flex;flex-direction:column;align-items:center;gap:16px}
  .mark__dot{width:110px;height:110px;border-radius:50%;background:var(--green)}
  .mark__name{font-family:'Questrial',sans-serif;font-size:30px;color:var(--blue);text-align:center;line-height:1.2}
</style>
</head>
<body>
<div class="canvas">

  <section class="card card--front">
    <div class="brand">
      <span class="brand__dot"></span>
      <span class="brand__name">Tidewell Vitality Mentor</span>
    </div>
    <p class="values">
      <span class="sep">•</span>Breathing <span class="sep">•</span>Meditation <span class="sep">•</span>Heartfelt intentional living <span class="sep">•</span>Oneness with others<br>
      <span class="sep">•</span>Compassion <span class="sep">•</span>Nutrition <span class="sep">•</span>Hydration and primary care physician.
    </p>
  </section>

  <section class="card card--back">
    <svg class="back-art" viewBox="0 0 880 503" preserveAspectRatio="none" aria-hidden="true">
      <defs>
        <radialGradient id="panelShade" cx="35%" cy="25%" r="80%">
          <stop offset="0" stop-color="#0a98d4"/>
          <stop offset="1" stop-color="#0567a3"/>
        </radialGradient>
      </defs>
      <path d="M0 0 H490 C430 140 440 330 560 503 H0 Z" fill="url(#panelShade)"/>
      <path d="M510 0 H530 C470 150 500 350 640 503 H600 C475 350 455 150 510 0 Z" fill="var(--green)"/>
    </svg>

    <div class="contact">
      <h1 class="contact__title"><span class="light">TIDEWELL</span><span class="bold">VITALITY<br>MENTOR</span></h1>
      <p class="contact__name">MARCUS R.T. DUNMORE</p>
      <p class="contact__role">CLP, CCHC, C-IQ<br>Tidewell Vitality Mentor</p>
      <p class="contact__address">614 Birchmoor Ave<br>Larkspur Heights, MI 48392</p>
      <p class="contact__line">
        <svg viewBox="0 0 24 24"><path fill="#fff" d="M3 9c0-3 4-5 9-5s9 2 9 5l-3 1-1-2c-3-1-7-1-10 0l-1 2zM7 11h10l2 8H5z"/></svg>
        023-5187-2294
      </p>
      <p class="contact__line">
        <svg viewBox="0 0 24 24"><rect x="2" y="5" width="20" height="14" fill="none" stroke="#fff" stroke-width="2"/><path d="M2 5l10 8 10-8" fill="none" stroke="#fff" stroke-width="2"/></svg>
        mentor@dunmorevitality.com
      </p>
    </div>

    <div class="mark">
      <span class="mark__dot"></span>
      <span class="mark__name">Tidewell Vitality Mentor</span>
    </div>
  </section>

</div>
</body>
</html>
```